Broschüren-Design für studentischen Personaldienstleister
Zielgruppe
KL Feldotrix ist ein studentischer Personaldienstleister, der seit 25 Jahren die IT- und Medien-Branche im Contentmanagement (Contentpflege, Redaktion, Grafik) und Onsiteservice (Floorwalking, Help Desk und Service Points) unterstützt.
Hierbei können wir auf das Know-how unserer Studenten vertrauen, die sich in der digitalen Landschaft zu Hause fühlen. Mit ihnen ergänzen wir bestehende Teams, wenn die eigene Crew ausgelastet ist oder keiner der internen Mitarbeiter Fachkenntnisse in dem erforderlichen Bereich mitbringt.
Zu unsere Kunden zählen insbesondere das Verlagswesen (Bsp. Henner-Wolmar SE), Digitalagenturen (Bsp. ORVA) und IT-Dienstleister (z.B Datavolkum AG).
Aufgabenstellung
Es soll ein 3-seitiges PDF/ erstellt werden, das NUR ONLINE versendet wird, es wird nicht gedruckt. Das Format kann frei gewählt werden, es soll modern und kreativ sein.
Zusätzlich soll ein Logo/Button entworfen werden, das auf allen Kanälen ausgespielt werden kann (jpg, png und eps.)
Für das 25-jährige-Jubiläum der Zusammenarbeit der Geschäftsführer, Tobias Wendrich und Lutz Hamerle, soll ein Mailing an Bestandskunden von KL Feldotrix versendet werden. Diesem Mailing soll ein PDF-Dokument/Flyer angehängt werden. Thematisch wird im Flyer der Claim “Klug. Vernetzt. Gemeinsam.” umgesetzt. Zusätzlich soll das bereits vorhandene Firmenlogo ein eigenes “Jubiläumsbranding” bekommen. Dieses Logo/Button soll sowohl im PDF eingebaut werden als auch zur weiteren thematischen Nutzung auf diversen sozialen Kanälen eingesetzt werden können.
SPEZIFIKATION PDF:
Umfang: 3 Seiten
Format: Kann offen gestaltet werden. Keine Vorgabe.
Inhalt: Die 3 Seiten spiegeln unseren Claim wieder. Auf jeder Seite soll ein „Fun Facts-Kasten“ eingebaut werden, der thematisch auflockert.
Design: Bitte verwenden sie unsere CI-Farben des Logos (HKS 44 + 50% Schwarz und HKS 92K). Logo fügen wir hier ein, Bild- und Textmaterial wird von uns gestellt und nach Zuschlag dem Gewinner zugesendet für die Fertigstellung des PDFs.
Seite 1: IM TEAM
Hier geht chronologisch um die Zusammenarbeit und Entstehung von KL Feldotrix GmbH. Kennenlerngeschichte. Start der Firma in Lüneburg. Zweites Büro in Berlin., neues CEO-Team mit drittem Geschäftsführer, KL Feldotrix heute.
Seite 2: SMART
Smart steht für unsere Studierenden. Warum wir mit studentischen Teams überzeugen. Wir liefern eine Win-Win-Situation mit fairen Konditionen für beide Situationen.
Feedback von unseren Studierenden. Beispiel für eine Erfolgsgeschichte, vom Studenten bei KL Feldotrix GmbH zur leitenden Position bei einem bekannten Medienunternehmen.
S..

```html
<!DOCTYPE html>
<html lang="de">
<head>
<meta charset="utf-8">
<title>KL Feldotrix – 6 gute Gründe</title>
<link rel="stylesheet" href="https://fonts.googleapis.com/css2?family=Montserrat:wght@600;700&family=Open+Sans:wght@400;600&display=swap">
<style>
  :root {
    --blue: #0f4a84;
    --blue-dark: #0b3a69;
    --grey: #6b6b6b;
    --grey-light: #8a8a8a;
    --paper: #f4f4f4;
    --text: #4a4a4a;
    --bg: #d9d9d9;
  }
  * { margin: 0; padding: 0; box-sizing: border-box; }
  html, body { width: 1200px; height: 851px; overflow: hidden; background: var(--bg); }
  .spread { position: relative; width: 1200px; height: 851px; display: flex; }
  .page { position: relative; width: 600px; height: 851px; background: var(--paper); overflow: hidden; }
  .page--left { border-right: 1px solid #d0d0d0; }
  .page-art { position: absolute; inset: 0; }
  .title {
    position: absolute; left: 40px; top: 44px;
    font-family: "Montserrat", sans-serif; font-weight: 700; font-size: 21px;
    color: var(--blue); letter-spacing: .3px;
  }
  .reasons {
    position: absolute; left: 40px; top: 92px; width: 530px;
    display: grid; grid-template-columns: 1fr 1fr; column-gap: 26px; row-gap: 14px;
    grid-auto-flow: column; grid-template-rows: repeat(3, auto);
  }
  .reason { display: flex; gap: 10px; }
  .reason__num {
    flex: none; width: 26px; height: 26px; border-radius: 50%; margin-top: 18px;
    background: var(--blue); color: #fff;
    font-family: "Montserrat", sans-serif; font-weight: 700; font-size: 14px;
    display: flex; align-items: center; justify-content: center;
  }
  .reason__title {
    font-family: "Montserrat", sans-serif; font-weight: 700; font-size: 11.5px;
    color: var(--blue); margin-bottom: 3px; text-transform: uppercase;
  }
  .reason__text {
    font-family: "Open Sans", sans-serif; font-size: 10.5px; line-height: 1.42;
    color: var(--text); text-align: justify;
  }
  .quotes { position: absolute; left: 70px; top: 380px; width: 480px; }
  .quote { display: flex; gap: 24px; align-items: flex-start; margin-bottom: 34px; }
  .quote__icon { flex: none; width: 70px; height: 70px; }
  .quote__text {
    font-family: "Open Sans", sans-serif; font-size: 11.5px; line-height: 1.45; color: var(--text);
  }
  .quote__text::before {
    content: "\201C"; font-family: "Montserrat", sans-serif; font-weight: 700;
    color: var(--blue); font-size: 18px; line-height: 0; margin-right: 5px; vertical-align: -4px;
  }
  .quote__name {
    display: block; margin-top: 14px; font-style: normal;
    font-family: "Montserrat", sans-serif; font-weight: 700; font-size: 12px; color: var(--blue);
  }
</style>
</head>
<body>
<main class="spread">

  <section class="page page--left">
    <svg class="page-art" width="600" height="851" viewBox="0 0 600 851">
      <defs>
        <linearGradient id="teamLaptop" x1="0" y1="0" x2="1" y2="1">
          <stop offset="0" stop-color="#c9b8a6"/>
          <stop offset=".55" stop-color="#7d8794"/>
          <stop offset="1" stop-color="#2f4f80"/>
        </linearGradient>
      </defs>
      <circle cx="470" cy="790" r="190" fill="var(--grey)"/>
      <path d="M -20 605 A 330 330 0 0 1 330 565" fill="none" stroke="var(--grey)" stroke-width="1.5"/>
      <circle cx="150" cy="533" r="9" fill="var(--blue)"/>
      <circle cx="325" cy="563" r="9" fill="var(--blue)"/>
      <circle cx="200" cy="835" r="290" fill="var(--blue)"/>
      <g role="img" aria-label="Foto: Studierende arbeiten gemeinsam an einem Laptop">
        <circle cx="200" cy="835" r="268" fill="url(#teamLaptop)"/>
      </g>
    </svg>

    <h1 class="title">6 GUTE GRÜNDE, BEI UNS ZU ARBEITEN</h1>

    <div class="reasons">
      <article class="reason">
        <span class="reason__num">1</span>
        <div>
          <h2 class="reason__title">Schnuppere Medienluft</h2>
          <p class="reason__text">Der Großteil unserer Studentenjobs findet im Umfeld der digitalen Medien statt. Ob du easy startest mit Contentpflege oder Datenmigration, direkt redaktionell und grafisch einsteigst oder digitale Neulinge coachst, hängt von deinem Talent und deinem Interesse ab.</p>
        </div>
      </article>
      <article class="reason">
        <span class="reason__num">2</span>
        <div>
          <h2 class="reason__title">Probiere dich aus</h2>
          <p class="reason__text">„Was willst du beruflich machen?“ Eine Frage, die gar nicht immer einfach zu beantworten ist. Bei uns kannst du dich in verschiedenen Bereichen ausprobieren und deiner Berufung näher kommen. Ohne Druck, dafür mit Spaß am Ausprobieren.</p>
        </div>
      </article>
      <article class="reason">
        <span class="reason__num">3</span>
        <div>
          <h2 class="reason__title">Vertiefe dein Wissen</h2>
          <p class="reason__text">In der Theorie meisterst du viele Aufgaben im Schlaf. Damit du deine Fachkenntnisse in die Praxis übertragen kannst, kommst du bei unseren Studentenjobs voll auf deine Kosten und erweiterst dein Spezialwissen, bis du Experte bist.</p>
        </div>
      </article>
      <article class="reason">
        <span class="reason__num">4</span>
        <div>
          <h2 class="reason__title">Arbeite, wann du willst</h2>
          <p class="reason__text">Da wir selbst studiert haben wissen wir, wie wichtig es ist, Arbeitszeiten passend zum Studienplan zu gestalten. Bei uns hast du ein großes Mitspracherecht bei der Gestaltung deines Dienstplans, damit dir genügend Zeit bleibt für Freizeit und Freunde.</p>
        </div>
      </article>
      <article class="reason">
        <span class="reason__num">5</span>
        <div>
          <h2 class="reason__title">Wir coachen und betreuen dich persönlich!</h2>
          <p class="reason__text">Natürlich erwarten wir von dir nicht, dass du sofort jedes System und alle Abläufe beherrscht, die beim Kunden wichtig sind. Deswegen begleiten wir jeden Start in ein neues Aufgabenfeld individuell, damit du beim ersten Kundeneinsatz sicher vorbereitet bist.</p>
        </div>
      </article>
      <article class="reason">
        <span class="reason__num">6</span>
        <div>
          <h2 class="reason__title">Wir bezahlen fair und zuverlässig!</h2>
          <p class="reason__text">Arbeiten, um zu leben ist out. Gerade im Studium möchtest du dir nicht nur zeitlich sondern auch finanziell etwas gönnen. Hierfür sind unsere übertariflich bezahlten Studentenjobs eine optimale Möglichkeit.</p>
        </div>
      </article>
    </div>
  </section>

  <section class="page page--right">
    <svg class="page-art" width="600" height="851" viewBox="0 0 600 851">
      <defs>
        <linearGradient id="teamThumbs" x1="0" y1="0" x2="1" y2="1">
          <stop offset="0" stop-color="#d8d3c8"/>
          <stop offset=".5" stop-color="#a8704f"/>
          <stop offset="1" stop-color="#3f8f8c"/>
        </linearGradient>
      </defs>
      <circle cx="130" cy="90" r="230" fill="var(--grey)"/>
      <path d="M 200 330 A 300 300 0 0 0 590 255" fill="none" stroke="var(--grey)" stroke-width="1.5"/>
      <circle cx="270" cy="336" r="9" fill="var(--blue)"/>
      <circle cx="495" cy="310" r="9" fill="var(--blue)"/>
      <circle cx="365" cy="150" r="190" fill="#f4f4f4"/>
      <circle cx="365" cy="150" r="180" fill="var(--blue)"/>
      <g role="img" aria-label="Foto: Gruppe Studierender in einer Bibliothek mit Daumen hoch">
        <circle cx="385" cy="135" r="160" fill="url(#teamThumbs)"/>
      </g>
    </svg>

    <div class="quotes">
      <figure class="quote">
        <svg class="quote__icon" viewBox="0 0 70 70" aria-hidden="true">
          <circle cx="35" cy="35" r="35" fill="var(--blue)"/>
          <path d="M20 26 h20 a6 6 0 0 1 6 6 v8 a6 6 0 0 1 -6 6 h-12 l-7 6 v-6 a6 6 0 0 1 -6 -6 v-8 a6 6 0 0 1 5 -6z" fill="none" stroke="#fff" stroke-width="2"/>
          <path d="M32 20 h16 a6 6 0 0 1 6 6 v8 a6 6 0 0 1 -6 6" fill="none" stroke="#fff" stroke-width="2"/>
        </svg>
        <blockquote class="quote__text">Generell möchte ich mich bei KL Feldotrix für die tolle Zeit bedanken! Ich habe viel gelernt und hatte auch viel Spaß bei all den verschiedenen Aufgaben.<cite class="quote__name">MIRA H.</cite></blockquote>
      </figure>
      <figure class="quote">
        <svg class="quote__icon" viewBox="0 0 70 70" aria-hidden="true">
          <circle cx="35" cy="35" r="35" fill="var(--blue)"/>
          <path d="M20 26 h20 a6 6 0 0 1 6 6 v8 a6 6 0 0 1 -6 6 h-12 l-7 6 v-6 a6 6 0 0 1 -6 -6 v-8 a6 6 0 0 1 5 -6z" fill="none" stroke="#fff" stroke-width="2"/>
          <path d="M32 20 h16 a6 6 0 0 1 6 6 v8 a6 6 0 0 1 -6 6" fill="none" stroke="#fff" stroke-width="2"/>
        </svg>
        <blockquote class="quote__text">Ein großes Dankeschön an euch und eure coole Organisation. Ich freue mich auf diese spannende Zeit und vor allem, dass ihr Studenten wie mir so eine tolle Gelegenheit gebt.<cite class="quote__name">JONAS V.</cite></blockquote>
      </figure>
      <figure class="quote">
        <svg class="quote__icon" viewBox="0 0 70 70" aria-hidden="true">
          <circle cx="35" cy="35" r="35" fill="var(--blue)"/>
          <path d="M20 26 h20 a6 6 0 0 1 6 6 v8 a6 6 0 0 1 -6 6 h-12 l-7 6 v-6 a6 6 0 0 1 -6 -6 v-8 a6 6 0 0 1 5 -6z" fill="none" stroke="#fff" stroke-width="2"/>
          <path d="M32 20 h16 a6 6 0 0 1 6 6 v8 a6 6 0 0 1 -6 6" fill="none" stroke="#fff" stroke-width="2"/>
        </svg>
        <blockquote class="quote__text">Danke für euer anhaltendes Verständnis und die Bemühungen, es uns allen, trotz Stundenplan-Chaos, immer recht zu machen.<cite class="quote__name">LENA V.</cite></blockquote>
      </figure>
    </div>
  </section>

</main>
</body>
</html>
```